Harbor Deed needs a new brochure design

The brochure will be used as a marketing tool for Realtors, Lenders and Family Law Attorney's. I have attached the "OLD" brochure to give you an idea of our business and what we do. We want a fresh more modern design. I also attached the Logo. Please let me know if you need any further information

Target Market(s)

Realtors, mortgage professionals (home lenders), Family Law Attorneys

```html
<!DOCTYPE html>
<html lang="en">
<head>
<meta charset="utf-8">
<title>Harbor Deed Brochure</title>
<link href="https://fonts.googleapis.com/css2?family=Raleway:wght@500;600&family=Roboto:wght@300;400;500&display=swap" rel="stylesheet">
<style>
:root{
  --brand:#2a5ec2;
  --brand-line:#3370c8;
  --navy:#1f3a8f;
  --ink:#3d3f45;
  --paper:#eef0f4;
  --white:#ffffff;
  --avatar-bg:#f6f7f9;
}
*{margin:0;padding:0;box-sizing:border-box}
html,body{width:1200px;height:1200px;overflow:hidden;background:var(--white)}
body{position:relative;font-family:'Roboto',sans-serif;color:var(--ink)}
.spread{position:absolute;left:0;top:176px;width:1200px;height:848px;
  background:linear-gradient(120deg,#f1f2f5 0%,#ece6e9 35%,#eef0f4 60%,#e9ecf0 100%);
  box-shadow:0 10px 14px -6px rgba(0,0,0,.35);overflow:hidden}
.shapes{position:absolute;left:0;top:0}
.photo{position:absolute}
.heading{font-family:'Raleway',sans-serif;font-weight:500}
.apart{position:absolute;left:25px;top:364px;width:365px}
.apart h2{font-size:26px;line-height:31px;color:var(--navy);margin-bottom:16px}
.apart p{font-size:11.8px;line-height:17.3px;font-weight:300;margin-bottom:16px}
.innovations{list-style:none}
.innovations li{position:relative;padding-left:32px;font-size:11.6px;line-height:15.3px;font-weight:300;margin-bottom:14px}
.innovations svg{position:absolute;left:1px;top:0}
.availability{position:absolute;left:25px;top:790px;font-size:13.6px;font-weight:500;color:#222}
.team-photo{position:absolute;background:var(--avatar-bg)}
.team-label{position:absolute;width:160px;text-align:center;font-size:12px;line-height:15px;color:var(--brand)}
.services{position:absolute;left:600px;top:334px;width:506px;height:520px;background:var(--brand);border-radius:20px 20px 0 0;color:var(--white)}
.services h2{font-size:27px;position:absolute}
.realtor-title{left:30px;top:18px}
.realtor-copy{position:absolute;left:30px;top:62px;width:412px;font-size:7.4px;line-height:12.6px;font-weight:300}
.realtor-copy p{margin-bottom:12.2px}
.lender-title{left:280px;top:244px}
.lender-copy{position:absolute;left:270px;top:284px;width:216px;text-align:center;font-size:7.4px;line-height:14.6px;font-weight:300}
</style>
</head>
<body>
<div class="spread">
  <svg class="shapes" width="1200" height="848" viewBox="0 176 1200 848">
    <polygon points="0,176 600,176 600,340 0,484" fill="#d6d9dd" role="img" aria-label="Photo of a consultant meeting a young couple at a laptop"/>
    <polygon points="0,484 600,340 600,348 0,520" fill="var(--brand)"/>
    <rect x="714" y="176" width="486" height="276" fill="#a9b3bd" role="img" aria-label="Photo of a handshake over a model house and keys"/>
    <path d="M694 176 V448 Q694 464 710 464 H1200" fill="none" stroke="var(--brand-line)" stroke-width="3"/>
    <path d="M600 494 H1112 Q1128 494 1128 510 V1024" fill="none" stroke="var(--brand-line)" stroke-width="3"/>
  </svg>

  <section class="apart">
    <h2 class="heading">What Sets Us Apart</h2>
    <p>At Harbor Deed,LLC,we understand the importance of having the sup-port of your Title Company whenever you need it.Because of this,we have developed cutting edge tools to help you provide the best service possible to your Buyers and Sellers.</p>
    <p>With over 11 years of experience in Title and Real Estate Law, we have the knowledge and follow through to ensure that your closing is suc-cessful and as headache free as possible.</p>
    <p style="margin-bottom:14px">Some of our innovations include:</p>
    <ul class="innovations">
      <li><svg width="18" height="18" viewBox="0 0 18 18"><circle cx="9" cy="9" r="9" fill="var(--navy)"/><path d="M5 9.3l2.7 2.6L13 6.5" fill="none" stroke="#fff" stroke-width="1.6"/></svg>Comprehensive Realtor/Lender Portal with<br>immediate secure access to documents and status updates.</li>
      <li><svg width="18" height="18" viewBox="0 0 18 18"><circle cx="9" cy="9" r="9" fill="var(--navy)"/><path d="M5 9.3l2.7 2.6L13 6.5" fill="none" stroke="#fff" stroke-width="1.6"/></svg>24/7 Net Sheet and Buyer Cost Estimator App<br>with the ability to Order Title with the click of a Button.</li>
      <li><svg width="18" height="18" viewBox="0 0 18 18"><circle cx="9" cy="9" r="9" fill="var(--navy)"/><path d="M5 9.3l2.7 2.6L13 6.5" fill="none" stroke="#fff" stroke-width="1.6"/></svg>Digital Closing Package for Buyers and Sellers with<br>secure online access to all closing documents post closing.</li>
      <li><svg width="18" height="18" viewBox="0 0 18 18"><circle cx="9" cy="9" r="9" fill="var(--navy)"/><path d="M5 9.3l2.7 2.6L13 6.5" fill="none" stroke="#fff" stroke-width="1.6"/></svg>Complimentary Post Closing Marketing Support for REAL-<br>TORS and Lenders!</li>
    </ul>
  </section>
  <div class="availability">Evening and Mobile Closings Available!</div>

  <div class="team-photo" style="left:433px;top:410px;width:122px;height:117px;background:linear-gradient(#f6f7f9,#c9d5e6)" role="img" aria-label="Portrait placeholder for the owner"></div>
  <div class="team-label" style="left:413px;top:535px">Owner</div>
  <div class="team-photo" style="left:433px;top:574px;width:120px;height:114px;background:linear-gradient(#f6f7f9,#9a9da2)" role="img" aria-label="Portrait placeholder for the director of sales and marketing"></div>
  <div class="team-label" style="left:413px;top:698px">Director Of<br>Sales and Marketing</div>

  <section class="services">
    <h2 class="heading realtor-title">Realtor Services</h2>
    <div class="realtor-copy">
      <p>We provide knowledge and support during the entire closing process to ensure a succesful transaction for you and your clients.</p>
      <p>Harbor Deed recognizes the importance of your reputation.Whether you are a seasoned agent with a high quality reputa-tion to protect or a new agent intent on building a respected name for yourself,Harbor Deed knows your livelihood de-pends on the quality of your name.Our title and escrow work is metculous, and our discretion second to none.</p>
      <p>We pride ourselves on timely,accurate communication and the trust that results from it.Our ability to tailor the transac-tion to you and your client is the bedrock of our company.</p>
      <p>Ask yourself what your current title company has done to contribute to your successlately?The importance of working with a stragically competitive agency in today's market has never been more essential to anyone's success.Harbor Deed has the experience,attention to detail and dedication to grow your bottom line.</p>
    </div>
    <div class="photo" style="left:29px;top:243px;width:203px;height:122px;background:linear-gradient(135deg,#e7ebf0,#2c3a5c)" role="img" aria-label="Photo of a lender shaking hands with a client"></div>
    <div class="photo" style="left:25px;top:376px;width:203px;height:122px;background:linear-gradient(#9aa3ab,#5d8a3e)" role="img" aria-label="Photo of an agent showing a house to a couple"></div>
    <h2 class="heading lender-title">Lender Services</h2>
    <div class="lender-copy">Harbor Deed works with national lenders,as well as local com-pany banks and moratage brokers<br>We have an extensive vendor network to ensure your client's transactions close on time with only the highest level of cus-tomer service.We handle all types of loans including Purchas-es,Refinances,1st and 2nd Mortages,HELOCs,Construction loans,FHA loans and VA loans.Our title services include:title search,title examination, title commitment,this clearence, payoff/lien orders escrow and closing services recording postclosing payoff tracking and title policy issuance.We are in full compliance with the Federal Consumer Lending Office regulations, as well as NTA Best Practices,and our ClearPath closing software is designed to promptly provide you with the most up to date fee and title information.</div>
  </section>
</div>
</body>
</html>
```